Re-design UI/UX for Online movie website

We need a stunning design for our online movie website www.vormalite.com

KALDORVUE is an online platform for the presentation of all visual art forms, particularly movies, feature films, short films, documentaries, game shows, reality shows, serials and traditional art forms of different languages for our international audience to indulge in.

We want a design & layout similar to leading online movie streaming websites such as Brimcast , Tavelo Crest , PLUMA BAY

Target Market(s)

Worldwide

Industry/Entity Type

Movie

Number of Pages Required

5+ page

Requirements
Must have
• Look & Feel - These are some of the suggestion. Please feel free to add as per industry standards. Be as creative as possible. The website needs to be really attractive. Movie listing , categories etc., should be easy to navigate
• 1 Text could be justified in all the pages
• 2 Font color may be changed to white color to be more visible.
• 3 Headings to be in Red color instead of Orange color. As Red will match the logo color as well
• 4 Heading to be consistent everywhere. Example in About us page " About us" font is capital, white in color and larger than the other 2 headings on the same page.
• 5 Chatterly, quibbr and Snapgrove links to be added
• 6 Menu options could be in white or red color to be more visible. Current grey color is looking dull.
• 8 One more menu tab to be included on the top named "Movies" or "Browse movies" . Under Browse Movies, add multilevel menu "New Releases" "Short Films" "Kaldorvue Originals" "Library" "All Movies" . Later categories like Comedy, Thriller etc, can be added
• 9 Add “Watch movie” or “Watch Trailer” on the banner Images
• 10 Give “back to home link” on all subpages
• 11 The Grid format showing movie thumbnails can be made better with border (red or white)

```html
<!DOCTYPE html>
<html lang="en">
<head>
<meta charset="utf-8">
<title>Kaldorvue – Personal Details</title>
<link href="https://fonts.googleapis.com/css2?family=Lato:wght@400;700&display=swap" rel="stylesheet">
<style>
:root{
  --page:#141414;
  --deep:#000000;
  --brand-red:#b5161b;
  --footer:#101010;
  --white:#ffffff;
  --text:#e6e6e6;
  --muted:#9a9a9a;
  --rule:#3a3a3a;
}
*{margin:0;padding:0;box-sizing:border-box}
html,body{width:1074px;height:1200px;overflow:hidden}
body{background:var(--page);font-family:'Lato',sans-serif;color:var(--text);position:relative}
.header-shape{position:absolute;left:0;top:0}
.brand{position:absolute;left:118px;top:30px;display:flex;align-items:center;gap:8px}
.brand-mark{width:14px;height:14px;background:var(--brand-red)}
.brand-name{font-size:26px;font-weight:700;color:var(--brand-red);letter-spacing:1px}
.nav{position:absolute;top:36px;font-size:11.5px;color:var(--white)}
.nav-caret{font-size:8px}
.welcome{position:absolute;left:770px;top:29px;width:150px;height:29px;background:var(--deep);display:flex;align-items:center}
.welcome-avatar{width:29px;height:29px;background:linear-gradient(#8b7a6a,#4a4038)}
.welcome-text{font-size:11.5px;color:var(--white);padding-left:9px}
.tv-button{position:absolute;left:928px;top:29px;width:28px;height:28px;border-radius:50%;background:var(--deep);display:flex;align-items:center;justify-content:center}

.profile-photo{position:absolute;left:118px;top:185px;width:162px;height:168px;background:linear-gradient(160deg,#cfcfcf,#8d8d8d)}
.profile-name{position:absolute;left:118px;top:362px;font-size:14px;color:var(--white)}
.profile-location{position:absolute;left:118px;top:385px;font-size:10.5px;color:var(--white)}
.side-menu{position:absolute;left:118px;top:410px;width:227px;list-style:none;border-top:1px solid var(--rule)}
.side-menu li{height:57.3px;border-bottom:1px solid var(--rule);display:flex;align-items:center;font-size:14.5px;color:var(--white);font-weight:400;letter-spacing:0.2px}
.side-menu li span{margin-right:8px}
.divider-red{position:absolute;left:366px;top:185px;width:2px;height:700px;background:var(--brand-red)}

.section-title{position:absolute;left:396px;top:180px;font-size:21px;font-weight:400;color:var(--white)}
.field-label{position:absolute;font-size:14px;font-weight:700;color:var(--white)}
.field-box{position:absolute;background:var(--deep);height:49px;display:flex;align-items:center;padding-left:20px;font-size:14.5px;color:var(--muted)}
.about-box{position:absolute;left:397px;top:251px;width:558px;height:136px;background:var(--deep);padding:16px 24px 0 20px;font-size:11.3px;line-height:21.6px;color:var(--muted)}

.footer{position:absolute;left:0;top:956px;width:1074px;height:244px;background:var(--footer)}
.footer-col{position:absolute;top:26px}
.footer-col h3{font-size:14px;font-weight:700;color:var(--white);margin-bottom:7px}
.footer-col li{list-style:none;font-size:9.5px;color:var(--text);line-height:20px}
.app-badge{position:absolute;left:817px;top:54px;width:138px;height:46px;background:#f2f2f2;border-radius:2px}
.footer-rule{position:absolute;left:118px;top:174px;width:838px;height:1px;background:var(--rule)}
.copyright{position:absolute;left:119px;top:203px;font-size:9.5px;color:var(--white)}
.social{position:absolute;top:202px;font-size:10px;color:var(--white)}
</style>
</head>
<body>

<svg class="header-shape" width="1074" height="114" viewBox="0 0 1074 114">
  <polygon points="0,0 300,0 344,86 368,86 378,113 0,113" fill="#000"/>
  <polygon points="300,0 1074,0 1074,86 344,86" fill="#b5161b"/>
</svg>

<div class="brand"><span class="brand-mark"></span><span class="brand-name">KALDORVUE</span></div>

<div class="nav" style="left:381px">Browse movies <span class="nav-caret">&#9662;</span></div>
<div class="nav" style="left:502px">About Us</div>
<div class="nav" style="left:582px">Terms of Service</div>
<div class="nav" style="left:698px">Contact</div>

<div class="welcome">
  <div class="welcome-avatar" role="img" aria-label="User avatar photo"></div>
  <div class="welcome-text">Welcome, Arlen Pike</div>
</div>
<div class="tv-button">
  <svg width="15" height="13" viewBox="0 0 15 13"><rect x="1" y="3" width="13" height="9" rx="1.5" fill="none" stroke="#fff" stroke-width="1.6"/><path d="M5 0.5 L7.5 3 L10 0.5" fill="none" stroke="#fff" stroke-width="1.3"/><rect x="10" y="5.5" width="2" height="4" fill="#fff"/></svg>
</div>

<div class="profile-photo" role="img" aria-label="Profile photo of the member"></div>
<div class="profile-name">Arlen Pike</div>
<div class="profile-location">Palakkad, Kerala</div>
<ul class="side-menu">
  <li><span>+</span>Personal Details</li>
  <li><span>+</span>Favourites (23)</li>
  <li><span>+</span>Likes (54)</li>
  <li><span>+</span>Messages (1)</li>
  <li><span>+</span>Channels</li>
  <li><span>+</span>Membership Details</li>
</ul>
<div class="divider-red"></div>

<h1 class="section-title">Personal Details</h1>
<div class="field-label" style="left:397px;top:226px">About Me</div>
<div class="about-box">Nulla tristique posuere molestie. Aliquam erat volutpat. Etiam quis aliquet risus. Duis ornare erat eget magna dapibus, in accumsan quam pharetra. Nam tempus, quam in bibendum vulputate, sapien dolor viverra nisl, vitae euismod elit turpis et nulla. Aliquam erat volutpat. Pellentesque blandit lacus eget nunc faucibus, et tincidunt eros viverra. Phasellus consequat sagittis nisi suscipit feugiat. Cras eget leo sed nunc hendrerit ultricies eu at nisl.</div>

<div class="field-label" style="left:397px;top:412px">Date of birth</div>
<div class="field-box" style="left:397px;top:437px;width:272px">June 5, 1990</div>
<div class="field-label" style="left:683px;top:412px">Gender</div>
<div class="field-box" style="left:683px;top:437px;width:272px">Male</div>

<div class="field-label" style="left:397px;top:512px">Phone</div>
<div class="field-box" style="left:397px;top:538px;width:558px">555 013 2847</div>
<div class="field-label" style="left:397px;top:607px">Email</div>
<div class="field-box" style="left:397px;top:633px;width:558px">info@arlen_pike.com</div>
<div class="field-label" style="left:397px;top:708px">City / State</div>
<div class="field-box" style="left:397px;top:733px;width:558px">Palakkad, Kerala</div>
<div class="field-label" style="left:397px;top:808px">Languages</div>
<div class="field-box" style="left:397px;top:833px;width:558px">Malayalam, Tamil, HIndi, English</div>

<footer class="footer">
  <div class="footer-col" style="left:119px"><h3>Donec interdum</h3><ul><li>Phasellus metus</li><li>Proin quis</li><li>Fusce quis</li><li>Donec venenatis</li><li>Aliquam mattis</li></ul></div>
  <div class="footer-col" style="left:300px"><h3>Nullam sit</h3><ul><li>Quisque pharetra</li><li>Cras interdum</li><li>Suspendisse</li><li>Sed iaculis</li><li>Duis mattis</li></ul></div>
  <div class="footer-col" style="left:464px"><h3>Phasellus lorem</h3><ul><li>Mauris ultrices</li><li>Mauris at</li><li>Proin rhoncus</li><li>Nullam varius</li><li>Sed efficitur</li></ul></div>
  <div class="footer-col" style="left:655px"><h3>Suspendisse</h3><ul><li>In sodales</li><li>Aliquam cursus</li><li>Fusce convallis</li><li>Curabitur</li><li>Vivamus dolor</li></ul></div>
  <div class="footer-col" style="left:816px"><h3>Download Apps</h3></div>
  <div class="app-badge" role="img" aria-label="App store download badge"></div>
  <div class="footer-rule"></div>
  <div class="copyright">Copyright &copy;&nbsp; 2018 &nbsp;KALDORVUE.&nbsp;&nbsp; All rights reserved.</div>
  <div class="social" style="left:820px">Chatterly</div>
  <div class="social" style="left:875px">quibbr</div>
  <div class="social" style="left:912px">Snapgrove</div>
</footer>

</body>
</html>
```